Graphics for Technology Company's Pennaroo Page

Need someone to create some graphics for our Pennaroo company page.
In particular, we're looking for:
- cover image
- Image for "overview"
- Image for "life"

I'd like you to take our logo and create professional graphics for our company Pennaroo page (https://www.pennaroo.net/company/7395081/).

Some examples of pages recognized by Pennaroo as top quality:
https://www.pennaroo.net/company/8574/
https://www.pennaroo.net/company/4718/
https://www.pennaroo.net/company/53720946/
https://www.pennaroo.net/company/8047352/

I especially like the last- zelquin. This is the kind of feel I'm looking for.

Target Market(s)

Medium and large businesses

Industry/Entity Type

Information Technology

Requirements
Must have
• The header should be proportional to 1536x768. Must use at least some of the colors in the logo and elements of the logo.
• Please note, this should be three distinct and thematically related images.

```html
<!DOCTYPE html>
<html lang="en">
<head>
<meta charset="utf-8">
<title>nQUARRY – Pennaroo page graphics</title>
<link rel="stylesheet" href="https://fonts.googleapis.com/css2?family=Fira+Sans:ital,wght@0,400;0,500;1,600&family=Fira+Sans+Condensed:wght@400&family=Roboto:wght@400;700&display=swap">
<style>
  :root {
    --canvas-bg: #d9d9d9;
    --panel-grey: #e9e9e9;
    --white: #ffffff;
    --ink: #111111;
    --ink-soft: #555555;
    --brand-green: #7fa62e;
    --brand-teal: #1b7f8f;
  }
  * { box-sizing: border-box; margin: 0; padding: 0; }
  html, body { width: 1200px; height: 1200px; overflow: hidden; }
  body { background: var(--canvas-bg); position: relative; font-family: "Fira Sans", sans-serif; }

  .page-header {
    position: absolute; left: 124px; top: 8px; width: 932px; height: 200px;
    background: var(--panel-grey);
    box-shadow: 6px 8px 14px rgba(0,0,0,.35);
  }
  .page-header__card {
    position: absolute; left: 20px; top: 14px; width: 896px; height: 178px;
    background: var(--white); border-bottom: 2px solid #cfcfcf;
  }
  .page-header__avatar {
    position: absolute; left: 30px; top: -14px; width: 166px; height: 168px;
    background:
      radial-gradient(ellipse 60% 50% at 50% 80%, rgba(200,240,245,.8), transparent 70%),
      linear-gradient(175deg, #0d3f4a 0%, #2f8ea0 45%, #7fc6d2 100%);
    box-shadow: 2px 3px 6px rgba(0,0,0,.4);
  }
  .page-header__avatar-band {
    position: absolute; left: 0; top: 62px; width: 100%; height: 26px;
    background: var(--white); display: flex; align-items: center; justify-content: center; gap: 6px;
    font: 400 17px "Fira Sans", sans-serif; color: var(--ink-soft); letter-spacing: .5px;
  }
  .page-header__info { position: absolute; left: 222px; top: 26px; font-family: "Roboto", sans-serif; }
  .page-header__name { font-size: 25px; font-weight: 700; color: var(--ink); }
  .page-header__meta { font-size: 18px; color: var(--ink-soft); line-height: 24px; margin-top: 2px; }
  .page-header__tabs {
    position: absolute; left: 222px; top: 150px; display: flex; gap: 14px;
    font: 700 18px "Roboto", sans-serif; color: var(--ink-soft);
  }
  .page-header__tab--active { color: var(--ink); border-bottom: 3px solid var(--ink); padding-bottom: 2px; }

  .banner {
    position: absolute; overflow: hidden;
    box-shadow: 6px 8px 14px rgba(0,0,0,.45);
  }
  .banner__photo { position: absolute; inset: 0; }
  .banner--cover { left: 122px; top: 208px; width: 934px; height: 308px; }
  .banner--cover .banner__photo {
    background:
      radial-gradient(ellipse 30% 45% at 80% 88%, rgba(235,250,252,.9), transparent 70%),
      radial-gradient(ellipse 22% 35% at 56% 95%, rgba(140,215,228,.8), transparent 70%),
      radial-gradient(ellipse 18% 30% at 97% 70%, rgba(10,60,70,.6), transparent 70%),
      radial-gradient(ellipse 40% 25% at 70% 40%, rgba(120,200,215,.6), transparent 70%),
      linear-gradient(180deg, #0c2a31 0%, #1a5866 18%, #2f8ea0 38%, #6cc0cf 65%, #b3e3ea 100%);
  }
  .banner--overview { left: 122px; top: 538px; width: 934px; height: 304px; }
  .banner--overview .banner__photo {
    background:
      radial-gradient(circle at 73% 56% , #3d6b74 0 5%, #1a3a41 7%, #5aa9b8 11%, #14323a 18%, #2a6977 24%, transparent 34%),
      radial-gradient(ellipse 25% 35% at 35% 70%, rgba(40,90,100,.5), transparent 70%),
      radial-gradient(ellipse 30% 40% at 25% 20%, rgba(250,253,253,.9), transparent 70%),
      linear-gradient(100deg, #eef7f8 0%, #b8e6ee 30%, #80d0de 55%, #4aa3b3 78%, #0e3a43 100%);
  }
  .banner--life { left: 120px; top: 864px; width: 938px; height: 312px; }
  .banner--life .banner__photo {
    background:
      radial-gradient(ellipse 45% 40% at 60% 85%, rgba(30,70,78,.55), transparent 70%),
      radial-gradient(ellipse 25% 40% at 90% 75%, rgba(35,75,82,.5), transparent 70%),
      radial-gradient(ellipse 30% 40% at 15% 85%, rgba(240,248,249,.9), transparent 70%),
      linear-gradient(110deg, #eaf4f5 0%, #9ccfd8 30%, #5e9ba6 55%, #406f78 80%, #2c4b52 100%);
  }

  .pill {
    position: absolute; left: 0; height: 48px;
    background: linear-gradient(180deg, #ffffff 0%, #f4f4f4 60%, #d8d8d8 100%);
    border-radius: 0 24px 24px 0;
    border-bottom: 3px solid var(--brand-green);
    border-right: 3px solid var(--brand-green);
    box-shadow: 3px 4px 6px rgba(0,0,0,.3);
    display: flex; align-items: center; white-space: nowrap;
  }
  .pill--brand { top: 30px; width: 447px; flex-direction: column; align-items: flex-start; justify-content: center; padding-left: 42px; }
  .pill--title { top: 125px; width: 343px; justify-content: center; }
  .pill--line { top: 220px; width: 398px; padding-left: 18px; }

  .brand-mark { display: flex; align-items: center; gap: 8px; }
  .brand-mark__square { width: 14px; height: 14px; background: var(--brand-green); }
  .brand-mark__name { font: 400 25px "Fira Sans", sans-serif; color: var(--ink-soft); letter-spacing: 1px; line-height: 26px; }
  .brand-tagline { font: 400 11px "Fira Sans", sans-serif; color: var(--brand-teal); letter-spacing: .3px; }

  .pill__text { font: 500 17px "Fira Sans", sans-serif; color: var(--ink); letter-spacing: .3px; }
  .pill__text--small { font: 400 14px "Fira Sans Condensed", sans-serif; color: var(--ink); letter-spacing: .1px; }
  .pill__text--life { font-size: 16px; }
  .pill__heading { font: italic 600 23px "Fira Sans", sans-serif; color: var(--ink); letter-spacing: .5px; margin-right: 40px; }
  .pill--title-left { justify-content: flex-start; padding-left: 18px; }
</style>
</head>
<body>

  <section class="page-header">
    <div class="page-header__card">
      <div class="page-header__avatar" role="img" aria-label="Teal-tinted composite of binary code and banknotes">
        <div class="page-header__avatar-band"><span class="brand-mark__square"></span>nQUARRY</div>
      </div>
      <div class="page-header__info">
        <div class="page-header__name">nQUARRY</div>
        <div class="page-header__meta">Computer-Software<br>11-50 Mitarbeiter</div>
      </div>
      <nav class="page-header__tabs">
        <span class="page-header__tab--active">Start</span>
        <span>Overview</span>
        <span>Life</span>
      </nav>
    </div>
  </section>

  <section class="banner banner--cover">
    <div class="banner__photo" role="img" aria-label="Teal-toned photo of streaming binary code above spread hundred-dollar banknotes"></div>
    <div class="pill pill--brand">
      <div class="brand-mark"><span class="brand-mark__square"></span><span class="brand-mark__name">nQUARRY</span></div>
      <div class="brand-tagline">Your Partner for Innovative Software Solutions</div>
    </div>
    <div class="pill pill--title pill--title-left">
      <span class="pill__text">Your business activity creates data.</span>
    </div>
    <div class="pill pill--line">
      <span class="pill__text">We turn data into dollars.</span>
    </div>
  </section>

  <section class="banner banner--overview">
    <div class="banner__photo" role="img" aria-label="Teal-toned close-up of an open hard drive platter and read arm over faint binary code"></div>
    <div class="pill pill--brand">
      <div class="brand-mark"><span class="brand-mark__square"></span><span class="brand-mark__name">nQUARRY</span></div>
      <div class="brand-tagline">Your Partner for Innovative Software Solutions</div>
    </div>
    <div class="pill pill--title"><span class="pill__heading">-OVERVIEW-</span></div>
    <div class="pill pill--line">
      <span class="pill__text--small">Relentless preparation. Robust solutions. Really good people.</span>
    </div>
  </section>

  <section class="banner banner--life">
    <div class="banner__photo" role="img" aria-label="Teal-toned silhouettes of a cheering crowd with raised arms over faint binary code"></div>
    <div class="pill pill--brand">
      <div class="brand-mark"><span class="brand-mark__square"></span><span class="brand-mark__name">nQUARRY</span></div>
      <div class="brand-tagline">Your Partner for Innovative Software Solutions</div>
    </div>
    <div class="pill pill--title"><span class="pill__heading">-LIFE-</span></div>
    <div class="pill pill--line">
      <span class="pill__text--small pill__text--life">We love helping other people solve their problems.</span>
    </div>
  </section>

</body>
</html>
```